11 x 17 Orvanthes Quote

Design the following quote in a poster.

"First say to yourself what you would be; then do what you have to do." - Orvanthes

See here for inspiration - https://prints.mornbrekal.com/

Quote

```html
<!DOCTYPE html>
<html lang="en">
<head>
<meta charset="utf-8">
<title>Orvanthes Quote Poster</title>
<link rel="stylesheet" href="https://fonts.googleapis.com/css2?family=Anton&display=swap">
<style>
  :root {
    --backdrop: #e9e8e6;
    --paper: #ffffff;
    --ink: #111111;
    --accent: #cc0009;
  }
  html, body {
    margin: 0;
    padding: 0;
    width: 1200px;
    height: 1148px;
    overflow: hidden;
    background: var(--backdrop);
  }
  .poster {
    position: absolute;
    left: 244px;
    top: 24px;
    width: 712px;
    height: 1100px;
    background: var(--paper);
    box-shadow: 0 2px 10px rgba(0,0,0,0.08);
  }
  .quote {
    position: absolute;
    left: 176px;
    top: 150px;
    margin: 0;
    font-family: "Anton", "Impact", sans-serif;
    font-weight: 400;
    text-transform: uppercase;
    font-size: 70px;
    line-height: 1;
    letter-spacing: 0.5px;
  }
  .quote-line {
    display: block;
    white-space: nowrap;
  }
  .quote-line--dark { color: var(--ink); }
  .quote-line--accent { color: var(--accent); }
  .quote-finale {
    display: flex;
    align-items: stretch;
    color: var(--accent);
    margin-top: 24px;
  }
  .quote-finale__word {
    font-size: 261px;
    line-height: 0.86;
    letter-spacing: -1px;
  }
  .quote-finale__side {
    display: flex;
    flex-direction: column;
    justify-content: space-between;
    padding: 14px 0 34px 10px;
  }
  .quote-finale__mark {
    font-size: 84px;
    line-height: 0.6;
  }
  .attribution {
    display: flex;
    align-items: center;
    gap: 6px;
    margin: 0;
    font-family: "Anton", "Impact", sans-serif;
    font-style: normal;
    font-weight: 400;
    font-size: 22px;
    line-height: 1;
    color: var(--ink);
    letter-spacing: 0.5px;
    text-transform: uppercase;
    white-space: nowrap;
  }
  .attribution__square {
    width: 17px;
    height: 17px;
    background: var(--ink);
  }
</style>
</head>
<body>
  <main class="poster">
    <blockquote class="quote">
      <span class="quote-line quote-line--dark">"First say to</span>
      <span class="quote-line quote-line--dark">yourself</span>
      <span class="quote-line quote-line--dark">what you</span>
      <span class="quote-line quote-line--dark">would be;</span>
      <span class="quote-line quote-line--accent">then do</span>
      <span class="quote-line quote-line--accent">what you</span>
      <span class="quote-line quote-line--accent">have to</span>
      <span class="quote-finale">
        <span class="quote-finale__word">Do</span>
        <span class="quote-finale__side">
          <span class="quote-finale__mark">"</span>
          <cite class="attribution"><span class="attribution__square"></span>Orvanthes</cite>
        </span>
      </span>
    </blockquote>
  </main>
</body>
</html>
```